i will be having a 2018 Brantel utility truck and i want to wrapTruck wrap

please look at the truck and current logo. we have supplied all the files
I have a red white and blue flag truck I would like to see something with our logo and cool design for the new truck we install gas pumps and repair gas station equipment.

Designs look the same

Low design quality

Please be creative i prefer a lighter background instead of dark back ground

Repair

• Must layout the truck that was provided in sample that is blank with no logo on it it is a van utility truck
• Phone number services provided on other truck that has logo thanks nice to have a american bald eagle with flag going toward he kovren logo or place it in a nice background
• Repair gas station equipment on it

```html
<!DOCTYPE html>
<html lang="en">
<head>
<meta charset="utf-8">
<title>Kovren Fuel Solutions – Utility Truck Wrap Layout</title>
<link rel="stylesheet" href="https://fonts.googleapis.com/css2?family=Barlow+Condensed:wght@500;600&display=swap">
<style>
  :root {
    --wrap-red: #c8202a;
    --wrap-navy: #272566;
    --wrap-white: #ffffff;
    --usdot-blue: #5b7fd0;
    --eagle-dark: #3a3270;
    --eagle-light: #b8423f;
    --page: #ffffff;
  }
  * { margin: 0; padding: 0; box-sizing: border-box; }
  html, body { width: 900px; height: 1200px; overflow: hidden; background: var(--page); }
  .sheet { position: relative; width: 900px; height: 1200px; }
  .panel { position: absolute; display: block; }
  .panel--driver-side { left: 70px; top: 40px; width: 760px; height: 279px; }
  .panel--passenger-side { left: 70px; top: 360px; width: 760px; height: 279px; }
  .panel--rear-doors { left: 110px; top: 690px; width: 330px; height: 359px; }
  .panel--cab-top { left: 490px; top: 690px; width: 300px; height: 117px; }
  .panel--hood { left: 490px; top: 840px; width: 300px; height: 134px; }
  .red { fill: var(--wrap-red); }
  .navy { fill: var(--wrap-navy); }
  .wrap-text { font-family: "Barlow Condensed", sans-serif; font-weight: 600; }
  .phone-light { fill: var(--wrap-white); }
  .phone-dark, .brand-name, .service-list { fill: var(--wrap-navy); }
  .usdot { fill: var(--usdot-blue); }
  .brand-mark { fill: var(--wrap-navy); }
</style>
</head>
<body>
<main class="sheet">
  <svg width="0" height="0" style="position:absolute">
    <defs>
      <linearGradient id="eagle-tone" x1="0" y1="0" x2="1" y2="1">
        <stop offset="0" stop-color="var(--eagle-light)"/>
        <stop offset="1" stop-color="var(--eagle-dark)"/>
      </linearGradient>
    </defs>
  </svg>

  <!-- Driver side -->
  <svg class="panel panel--driver-side" viewBox="0 0 703 258" aria-label="Driver side wrap panel">
    <polygon class="red" points="0,0 168,0 0,205"/>
    <polygon class="red" points="0,258 0,230 70,160 40,258"/>
    <polygon class="navy" points="25,258 130,120 70,258"/>
    <polygon class="red" points="80,258 150,140 120,258"/>
    <polygon class="red" points="221,258 262,258 370,80 355,80"/>
    <polygon class="navy" points="278,258 388,0 565,0 458,258" role="img" aria-label="Star field of the flag"/>
    <polygon class="red" points="450,258 472,258 492,200"/>
    <polygon class="navy" points="570,190 625,105 600,225"/>
    <polygon class="red" points="555,258 600,258 703,150 700,120"/>
    <rect x="240" y="8" width="140" height="82" rx="30" fill="url(#eagle-tone)" role="img" aria-label="Bald eagle with flag-patterned wings flying toward the brand name"/>
    <text class="wrap-text phone-light" x="15" y="38" font-size="24">555-014-2270</text>
    <text class="wrap-text phone-light" x="15" y="62" font-size="11">· MD 3rd Party Inspections</text>
    <text class="wrap-text phone-light" x="15" y="76" font-size="11">· Tank and Line Testing</text>
    <text class="wrap-text phone-light" x="15" y="90" font-size="11">· Service and Repair</text>
    <circle class="brand-mark" cx="205" cy="62" r="22"/>
    <text class="wrap-text brand-name" x="205" y="106" font-size="20" text-anchor="middle">KOVREN FUEL</text>
    <text class="wrap-text brand-name" x="205" y="120" font-size="11" text-anchor="middle">SOLUTIONS, INC.</text>
    <text class="wrap-text usdot" x="158" y="202" font-size="15">USDOT 4410582</text>
    <circle class="brand-mark" cx="523" cy="172" r="10"/>
    <text class="wrap-text brand-name" x="523" y="198" font-size="11" text-anchor="middle">KOVREN FUEL</text>
    <text class="wrap-text phone-dark" x="523" y="225" font-size="13" text-anchor="middle">555-014-2270</text>
  </svg>

  <!-- Passenger side -->
  <svg class="panel panel--passenger-side" viewBox="0 0 703 258" aria-label="Passenger side wrap panel">
    <g transform="translate(703,0) scale(-1,1)">
      <polygon class="red" points="0,0 168,0 0,205"/>
      <polygon class="red" points="0,258 0,230 70,160 40,258"/>
      <polygon class="navy" points="25,258 130,120 70,258"/>
      <polygon class="red" points="80,258 150,140 120,258"/>
      <polygon class="red" points="221,258 262,258 370,80 355,80"/>
      <polygon class="navy" points="278,258 388,0 565,0 458,258" role="img" aria-label="Star field of the flag"/>
      <polygon class="red" points="450,258 472,258 492,200"/>
      <polygon class="navy" points="570,190 625,105 600,225"/>
      <polygon class="red" points="555,258 600,258 703,150 700,120"/>
    </g>
    <rect x="323" y="8" width="140" height="82" rx="30" fill="url(#eagle-tone)" role="img" aria-label="Bald eagle with flag-patterned wings flying toward the brand name"/>
    <text class="wrap-text phone-light" x="688" y="38" font-size="24" text-anchor="end">555-014-2270</text>
    <text class="wrap-text phone-light" x="688" y="62" font-size="11" text-anchor="end">· MD 3rd Party Inspections</text>
    <text class="wrap-text phone-light" x="688" y="76" font-size="11" text-anchor="end">· Tank and Line Testing</text>
    <text class="wrap-text phone-light" x="688" y="90" font-size="11" text-anchor="end">· Service and Repair</text>
    <circle class="brand-mark" cx="498" cy="62" r="22"/>
    <text class="wrap-text brand-name" x="498" y="106" font-size="20" text-anchor="middle">KOVREN FUEL</text>
    <text class="wrap-text brand-name" x="498" y="120" font-size="11" text-anchor="middle">SOLUTIONS, INC.</text>
    <text class="wrap-text usdot" x="450" y="202" font-size="15">USDOT 4410582</text>
    <circle class="brand-mark" cx="180" cy="172" r="10"/>
    <text class="wrap-text brand-name" x="180" y="198" font-size="11" text-anchor="middle">KOVREN FUEL</text>
    <text class="wrap-text phone-dark" x="180" y="225" font-size="13" text-anchor="middle">555-014-2270</text>
  </svg>

  <!-- Rear doors -->
  <svg class="panel panel--rear-doors" viewBox="0 0 450 490" aria-label="Rear doors wrap panel">
    <polygon class="red" points="0,0 200,0 0,330"/>
    <polygon class="navy" points="0,375 0,340 135,120"/>
    <polygon class="red" points="0,455 0,400 95,270"/>
    <polygon class="red" points="330,215 450,165 450,250"/>
    <polygon class="red" points="270,490 345,370 310,490"/>
    <polygon class="navy" points="320,490 450,250 450,490" role="img" aria-label="Star field of the flag"/>
    <rect x="230" y="0" width="220" height="160" rx="60" fill="url(#eagle-tone)" role="img" aria-label="Bald eagle with flag-patterned wings swooping toward the brand name"/>
    <circle class="brand-mark" cx="225" cy="150" r="35"/>
    <text class="wrap-text brand-name" x="225" y="240" font-size="32" text-anchor="middle">KOVREN FUEL</text>
    <text class="wrap-text brand-name" x="225" y="266" font-size="18" text-anchor="middle">SOLUTIONS, INC.</text>
    <text class="wrap-text phone-dark" x="225" y="320" font-size="46" text-anchor="middle">555-014-2270</text>
    <text class="wrap-text service-list" x="225" y="356" font-size="18" text-anchor="middle">· MD 3rd Party Inspections</text>
    <text class="wrap-text service-list" x="225" y="374" font-size="18" text-anchor="middle">· Tank and Line Testing</text>
    <text class="wrap-text service-list" x="225" y="392" font-size="18" text-anchor="middle">· Service and Repair</text>
  </svg>

  <!-- Cab top -->
  <svg class="panel panel--cab-top" viewBox="0 0 447 175" aria-label="Cab top wrap panel">
    <polygon class="red" points="0,0 140,0 0,140"/>
    <polygon class="navy" points="0,175 0,150 110,60 40,175"/>
    <polygon class="red" points="55,175 130,80 95,175"/>
    <polygon class="red" points="305,175 420,20 440,20 340,175"/>
    <polygon class="navy" points="350,175 447,30 447,175" role="img" aria-label="Star field of the flag"/>
    <rect x="270" y="0" width="150" height="85" rx="35" fill="url(#eagle-tone)" role="img" aria-label="Bald eagle with flag-patterned wings"/>
    <circle class="brand-mark" cx="225" cy="55" r="20"/>
    <text class="wrap-text brand-name" x="225" y="112" font-size="22" text-anchor="middle">KOVREN FUEL</text>
    <text class="wrap-text brand-name" x="225" y="128" font-size="12" text-anchor="middle">SOLUTIONS, INC.</text>
  </svg>

  <!-- Hood -->
  <svg class="panel panel--hood" viewBox="0 0 447 200" aria-label="Hood wrap panel">
    <polygon class="red" points="0,0 90,20 0,120"/>
    <polygon class="red" points="30,200 110,40 70,200"/>
    <polygon class="navy" points="0,180 0,150 100,50"/>
    <polygon class="red" points="305,200 400,60 425,50 340,200"/>
    <polygon class="navy" points="355,200 447,0 447,200" role="img" aria-label="Star field of the flag"/>
    <rect x="250" y="50" width="140" height="80" rx="35" fill="url(#eagle-tone)" role="img" aria-label="Bald eagle with flag-patterned wings"/>
    <circle class="brand-mark" cx="220" cy="100" r="24"/>
    <text class="wrap-text brand-name" x="220" y="165" font-size="26" text-anchor="middle">KOVREN FUEL</text>
    <text class="wrap-text brand-name" x="220" y="183" font-size="14" text-anchor="middle">SOLUTIONS, INC.</text>
  </svg>
</main>
</body>
</html>
```